Helicopter Tour Brochure Design (8.5 x 11" Bi-Fold Brochure)

Flyer Design for Helicopter Sightseeing Tours. Should be very inviting and touristy. Read "must have" section for more information.

Target Market(s)

Tourists visiting Florida

Industry/Entity Type

Aviation

Colors
3176b5
0456a4
85acd3
757575
9d9d9d
1b1b1b

Requirements
Must have
• Must include the Tour photos and "Route map", so customers know where the tours travels along. It must be inviting.
• Also, design must be for a 8.5 x 11" bi-fold brochure/flyer and include a brief description about our company:
• " Corvane Aviation offers unparalleled sightseeing opportunities with a commitment to safety & customer service. The view during our sightseeing tours will provide for your comfort & more beauty than you ever imagined. And like many of our customers, you’ll want to tell your friends all about it! Corvane Aviation’s experienced pilots will provide a comfortable flight leaving you with a smile on your face. Departure location will be the Pellmont Airport, unless otherwise requested with our office. "
• You can find the tour description online at www.corvanetx.com/tours, which should be included as well.
• Must be in PDF Format.
• 8.5 x 11" Bi-Fold Brochure
• ATTACHED ARE THE DETAILED FORMAT INFORMATION.

```html
<!DOCTYPE html>
<html lang="en">
<head>
<meta charset="utf-8">
<title>Corvane Aviation – Helicopter Tours Brochure</title>
<link href="https://fonts.googleapis.com/css2?family=Tinos:wght@400;700&display=swap" rel="stylesheet">
<style>
  :root{
    --sky:#8fb1d7;
    --sky-pale:#c3d7ec;
    --brand:#3176b5;
    --deep:#0456a4;
    --ink:#1b1b1b;
    --rule:#1b1b1b;
    --white:#ffffff;
    --map-water:#d9e4ef;
    --map-land:#efece2;
  }
  html,body{margin:0;padding:0;overflow:hidden;background:#fff;}
  .canvas{position:relative;width:1200px;height:1000px;overflow:hidden;background:#fff;font-family:"Tinos","Times New Roman",serif;color:var(--ink);}
  .sheet{position:absolute;left:30px;top:55px;width:1140px;height:880px;overflow:hidden;background:var(--sky);}
  .sheet-waves{position:absolute;left:0;top:0;width:1140px;height:880px;}
  .block{position:absolute;margin:0;}
  .tour-title{font-size:22px;font-weight:400;margin:0;line-height:1;white-space:nowrap;}
  .body-copy{font-size:14.5px;line-height:18.9px;margin:0;}
  .route-map{position:absolute;background:linear-gradient(135deg,var(--map-water) 0%,var(--map-land) 60%,var(--map-water) 100%);border:1px solid #e6e6e6;}
  .photo{position:absolute;}
  .photo-marina{background:linear-gradient(180deg,#5a8fc9 0%,#9fc1e0 35%,#d9c6a2 55%,#2f6f9a 75%,#1e5a86 100%);}
  .photo-skyline{background:linear-gradient(180deg,#0f2f6b 0%,#2c5aa8 35%,#d98a5a 52%,#1d2b48 62%,#3a3326 80%,#1a1f2a 100%);}
  .brand-name{font-size:54px;font-weight:700;color:var(--brand);line-height:1;white-space:nowrap;}
  .brand-square{display:inline-block;width:14px;height:14px;background:var(--brand);margin-left:8px;vertical-align:middle;}
  .contact{font-size:14.5px;line-height:19px;white-space:nowrap;}
  .divider{position:absolute;left:598px;top:157px;width:517px;height:1px;background:var(--rule);}
  .link{color:var(--white);}
</style>
</head>
<body>
<div class="canvas">
  <div class="sheet">
    <svg class="sheet-waves" viewBox="0 0 1140 880" aria-hidden="true">
      <defs>
        <linearGradient id="swoosh" x1="0" y1="0" x2="1" y2="0">
          <stop offset="0" stop-color="#8fb1d7"/>
          <stop offset="0.5" stop-color="#b3cde8"/>
          <stop offset="1" stop-color="#c3d7ec"/>
        </linearGradient>
      </defs>
      <path d="M0,295 C220,330 420,470 600,505 C800,540 1000,515 1140,478 L1140,880 L0,880 Z" fill="#0456a4"/>
      <path d="M300,380 C420,450 500,495 600,505 C800,530 1000,510 1140,478 L1140,250 L300,250 Z" fill="url(#swoosh)" opacity="0.6"/>
    </svg>

    <h2 class="tour-title block" style="left:57px;top:45px;">The Downtown &amp; Romantic Tour</h2>
    <p class="body-copy block" style="left:57px;top:72px;width:228px;">(Approx. 20-Minute flight time) Experience the beauty of Downtown Pellmont including an up-close view of the Ashgrove Art Museum, Delmore Performing Arts Hall, the Baywater Grand, Ashgrove Bridge and Gull Key. The Tour travels around Marlow Circle and as the mainland approaches the Marina and a true landmark office building, Harbor One in Pellmont’s central business district are just ahead.</p>
    <div class="route-map" style="left:302px;top:80px;width:238px;height:301px;" role="img" aria-label="Route map of the Downtown and Romantic Tour along the bay and keys"></div>

    <h2 class="tour-title block" style="left:57px;top:389px;">The Deluxe Tour</h2>
    <div class="route-map" style="left:57px;top:423px;width:237px;height:308px;" role="img" aria-label="Route map of the Deluxe Tour along the full coastline and keys"></div>
    <p class="body-copy block" style="left:318px;top:525px;width:222px;text-align:right;">(Approx. 1-Hour flight time) This special VIP Tour combines all the sights of our DOWNTOWN and ULTIMATE BEACH Tours and is our most exciting and exhilarating sightseeing option with many great locations and landmarks. This flight provides the opportunity to see virtually the entire Pellmont coastline with a trip across Alder Bay along Skyline Causeway Bridge and Port Alder Downtown.</p>

    <p class="body-copy block" style="left:57px;top:776px;width:480px;">Please visit our website: <span class="link">www.corvanetx.com/tours</span> to see our complete selection of helicopter tours, services and prices. Tours can be purchased on the website for your convenience.</p>

    <p class="brand-name block" style="left:598px;top:62px;">Corvane<span class="brand-square"></span></p>
    <p class="contact block" style="left:862px;top:54px;">Corvane Aviation Texas, LLC<br>(and Bluewing Rotorcraft, LLC)<br>Pellmont Regional Airport (KPLM)<br>4270 Harbor Vista Road, Hangar C-3<br>Pellmont, TX 77590 United States</p>
    <div class="divider"></div>
    <p class="contact block" style="left:598px;top:166px;">Phone: +1 (409) 555-0188<br>Email: info@corvanetx.com</p>
    <p class="contact block" style="left:780px;top:166px;width:306px;text-align:right;">Website: http://corvanetx.com/tours/<br>Social Media: @CorvaneAviationTX</p>

    <p class="body-copy block" style="left:598px;top:272px;width:490px;"><span style="float:right;width:268px;height:152px;"></span>Corvane Aviation offers unparalleled sightseeing opportunities with a commitment to safety &amp; customer service. The view during our sightseeing tours will provide for your comfort &amp; more beauty than you ever imagined. And like many of our customers, you’ll want to tell your friends all about it! Corvane Aviation’s experienced pilots will provide a comfortable flight leaving you with a smile on your face. Departure location will be the Pellmont Airport, unless otherwise requested with our office.</p>
    <div class="photo photo-marina" style="left:835px;top:270px;width:251px;height:160px;" role="img" aria-label="Aerial photo of waterfront condominium towers on a bay island"></div>

    <div class="photo photo-skyline" style="left:570px;top:508px;width:542px;height:346px;" role="img" aria-label="Twilight aerial photo of the downtown skyline and bay"></div>
  </div>
</div>
</body>
</html>
```